Local Electrician domestic work

I want a flyer to distribute locally for the replacement of old asbestos switchboards. I want a picture of an old board and one that I have replaced. It needs to say that all relevant standards will be met and the asbestos will be removed and disposed of in accordance with all Coastal Waste Oversight Board guidelines.
I also want on there a section that will tell them what other work I do which includes solar installations and maintenance, level 2 electrical work, all general domestic electrical work and emergency callouts.
I want the colour scheme to work with my company logo of orange and blue.
Target Market(s)
Home Owners that are living in older homes
Industry/Entity Type
Electrical

```html
<!DOCTYPE html>
<html lang="en">
<head>
<meta charset="utf-8">
<title>Ridgeway Electrical – Flyers</title>
<link href="https://fonts.googleapis.com/css2?family=Mulish:wght@400;600;800;900&display=swap" rel="stylesheet">
<style>
  :root{
    --blue:#2d5fa6;
    --orange:#e2712a;
    --sky:#dcebf7;
    --sky-deep:#b9d6ee;
    --paper:#f7fbfe;
    --bg:#eeeae4;
  }
  *{box-sizing:border-box;margin:0;padding:0}
  html,body{width:1200px;height:1000px;overflow:hidden}
  body{background:var(--bg);font-family:"Mulish",Arial,sans-serif;position:relative}

  .flyer{
    position:absolute;width:560px;height:400px;
    background:linear-gradient(100deg,var(--paper) 0%,#eaf3fb 45%,var(--sky) 100%);
    box-shadow:0 10px 24px rgba(0,0,0,.22);overflow:hidden;
  }
  .flyer--switchboard{left:27px;top:300px}
  .flyer--services{left:613px;top:300px}

  .flyer__top-band{position:absolute;left:0;top:0;width:100%;height:26px;background:var(--blue)}
  .flyer__swoosh{position:absolute;left:0;top:26px;width:100%;height:282px}
  .flyer__bottom-band{
    position:absolute;left:0;bottom:0;width:100%;height:92px;background:var(--orange);
    display:flex;align-items:center;justify-content:space-between;padding:0 26px;color:#fff;
  }

  .main-column{position:absolute;left:26px;top:42px;width:270px;display:flex;flex-direction:column;gap:14px}

  .brand{display:flex;align-items:center;gap:12px}
  .brand__dot{width:40px;height:40px;border-radius:50%;background:var(--orange);flex:none}
  .brand__name{font-weight:900;font-size:24px;line-height:1;color:var(--blue);letter-spacing:.5px;text-transform:uppercase}

  .headline{font-weight:900;color:var(--blue);text-transform:uppercase;line-height:1.15;font-size:18px}
  .tagline{font-weight:800;font-size:13px;color:var(--blue);margin-bottom:-8px}
  .body-copy{font-size:11.5px;line-height:1.5;color:var(--blue);font-weight:400}
  .body-copy strong{font-weight:800}

  .quote__label{font-size:11px;font-weight:800;letter-spacing:.5px;text-transform:uppercase}
  .quote__phone{font-size:30px;font-weight:900;letter-spacing:.5px;line-height:1.1}
  .address{font-size:12.5px;font-weight:800;line-height:1.4;width:230px}

  .side-column{position:absolute;left:306px;top:36px;width:234px;display:flex;flex-direction:column;gap:10px}
  .compare{display:flex;gap:12px}
  .compare__item{display:flex;flex-direction:column;gap:4px}
  .compare__label{font-size:10px;font-weight:900;color:var(--orange);text-transform:uppercase}
  .compare__photo{width:111px;height:132px;border-radius:10px;border:4px solid #fff;box-shadow:0 3px 8px rgba(0,0,0,.25)}
  .compare__photo--before{background:linear-gradient(160deg,#8a8a86,#3e3e3c)}
  .compare__photo--after{background:linear-gradient(160deg,#c9ccd0,#2f3236)}
  .standards{font-size:10.5px;line-height:1.45;color:var(--blue);font-weight:600}

  .hero-photo{position:absolute;right:0;top:26px;width:240px;height:282px;
    background:linear-gradient(160deg,#dfe9f3 0%,#c7d3de 45%,#f2f4f6 70%,#b9c3cc 100%)}
</style>
</head>
<body>

<section class="flyer flyer--switchboard">
  <div class="flyer__top-band"></div>
  <svg class="flyer__swoosh" viewBox="0 0 560 282" preserveAspectRatio="none" aria-hidden="true">
    <path d="M0 230 C160 150 320 260 560 120 L560 150 C320 280 160 180 0 250Z" fill="#fff" opacity=".6"/>
    <path d="M200 282 C320 200 440 220 560 160 L560 282Z" fill="var(--sky-deep)" opacity=".35"/>
  </svg>

  <div class="main-column">
    <div class="brand"><span class="brand__dot"></span><span class="brand__name">Ridgeway<br>Electrical</span></div>
    <h1 class="headline">Does your switchboard<br>look like this?</h1>
    <p class="body-copy">It has likely been made using asbestos!<br>At <strong>Ridgeway Electrical</strong> we can replace your switchboard to bring it up to current standards and remove the asbestos for you.</p>
  </div>

  <div class="side-column">
    <div class="compare">
      <div class="compare__item">
        <span class="compare__label">Before</span>
        <div class="compare__photo compare__photo--before" role="img" aria-label="Photo of an old asbestos switchboard"></div>
      </div>
      <div class="compare__item">
        <span class="compare__label">After</span>
        <div class="compare__photo compare__photo--after" role="img" aria-label="Photo of a newly replaced modern switchboard"></div>
      </div>
    </div>
    <p class="standards">All relevant standards will be met and the asbestos will be removed and disposed of in accordance with all Coastal Waste Oversight Board guidelines.</p>
  </div>

  <div class="flyer__bottom-band">
    <div class="quote">
      <div class="quote__label">Call for a free quote!</div>
      <div class="quote__phone">0400 555 172</div>
    </div>
    <div class="address">PO Box 41 Seacliff,<br>New South Wales, Australia 2599</div>
  </div>
</section>

<section class="flyer flyer--services">
  <div class="flyer__top-band"></div>
  <svg class="flyer__swoosh" viewBox="0 0 560 282" preserveAspectRatio="none" aria-hidden="true">
    <path d="M0 230 C160 150 320 260 560 120 L560 150 C320 280 160 180 0 250Z" fill="#fff" opacity=".6"/>
  </svg>
  <div class="hero-photo" role="img" aria-label="Photo of a smiling electrician in a hard hat standing beside a branded white work van"></div>

  <div class="main-column" style="width:290px">
    <div class="brand"><span class="brand__dot"></span><span class="brand__name">Ridgeway<br>Electrical</span></div>
    <h2 class="headline">Local electrician servicing<br>the Illawarra region.</h2>
    <p class="tagline">No job too big or too small.</p>
    <p class="body-copy">Experience in solar installations and maintenance, level 2 electrical work, all general domestic electrical work and emergency callouts.</p>
  </div>

  <div class="flyer__bottom-band">
    <div class="quote">
      <div class="quote__label">Call for a free quote!</div>
      <div class="quote__phone">0400 555 172</div>
    </div>
  </div>
</section>

</body>
</html>
```